Velmora KQRX Magazine Cover style graphic.

I am looking to create a document cover.
Brandell Solutions
The True Cost of an Embroidery Machineā€
Subtitle: Why the Lowest Upfront Price Can Become the Most Expensive Decision. Using Brandell logo's and Velmora KQRX for a high impact cover. It should look like a magazine cover. This is the most advance technology available for the embroidery industry. We want to portray this as a platform and not simply a machine. We will have an 8 page guide.

Target Market(s)

Our customer base

Industry/Entity Type

Industrial Embroidery

Font styles to use
Serif

Colors
0054AA
0677BA
7BADD7
CADEEF
E8F1F8

Requirements
Must have
• High impact, visually pleasing cover.

```html
<!DOCTYPE html>
<html lang="en">
<head>
<meta charset="utf-8">
<title>The True Cost of an Embroidery Machine – Brandell Solutions</title>
<link rel="stylesheet" href="https://fonts.googleapis.com/css2?family=Bebas+Neue&family=Montserrat:wght@700&family=Spectral:wght@300&display=swap">
<style>
  :root {
    --page-bg: #555555;
    --paper: #ffffff;
    --ink: #111111;
    --pink: #e4307a;
    --pink-deep: #b3245f;
    --teal: #178b7a;
    --blue-deep: #0054aa;
    --blue-mid: #0677ba;
    --blue-soft: #7badd7;
    --blue-band: #6bb5da;
    --machine-light: #e6e7e8;
    --machine-shade: #c9cbcd;
  }
  * { margin: 0; padding: 0; box-sizing: border-box; }
  html, body { width: 1200px; height: 1200px; overflow: hidden; }
  body { background: var(--page-bg); position: relative; }

  .cover {
    position: absolute;
    left: 295px; top: 168px;
    width: 610px; height: 865px;
    background: var(--paper);
    overflow: hidden;
  }
  .cover-art { position: absolute; inset: 0; width: 610px; height: 865px; }

  .brand {
    position: absolute;
    display: flex; align-items: center; gap: 6px;
    font-family: "Montserrat", sans-serif;
    font-weight: 700;
    line-height: 1;
  }
  .brand-primary { left: 36px; top: 40px; font-size: 15px; color: var(--ink); }
  .brand-primary .brand-mark {
    width: 36px; height: 36px; background: var(--blue-mid);
  }
  .brand-partner { left: 522px; top: 52px; font-size: 12px; color: var(--paper); letter-spacing: 0.5px; }

  .title {
    position: absolute;
    left: 36px; top: 198px;
    font-family: "Bebas Neue", sans-serif;
    font-size: 69px;
    line-height: 66px;
    font-weight: 400;
    color: var(--ink);
  }
  .title span { display: block; }
  .title .accent-pink { color: var(--pink); }
  .title .accent-teal { color: var(--teal); }

  .subtitle {
    position: absolute;
    left: 36px; top: 546px;
    width: 200px;
    font-family: "Spectral", serif;
    font-weight: 300;
    font-size: 19px;
    line-height: 31.5px;
    color: var(--ink);
  }
</style>
</head>
<body>
  <article class="cover">
    <svg class="cover-art" viewBox="0 0 610 865" xmlns="http://www.w3.org/2000/svg">
      <defs>
        <linearGradient id="blueTeal" x1="0" y1="1" x2="1" y2="0">
          <stop offset="0" stop-color="#128a7c"/>
          <stop offset="0.5" stop-color="#14608f"/>
          <stop offset="1" stop-color="#23389a"/>
        </linearGradient>
        <linearGradient id="pinkGlow" x1="0" y1="0" x2="1" y2="1">
          <stop offset="0" stop-color="var(--pink)"/>
          <stop offset="1" stop-color="var(--pink-deep)"/>
        </linearGradient>
        <linearGradient id="machineTone" x1="0" y1="0" x2="0" y2="1">
          <stop offset="0" stop-color="var(--machine-light)"/>
          <stop offset="1" stop-color="var(--machine-shade)"/>
        </linearGradient>
      </defs>

      <rect class="fabric-band" x="0" y="804" width="610" height="61" fill="var(--blue-band)" role="img" aria-label="Blue embroidered fabric texture"/>

      <circle class="feature-disc" cx="469" cy="161" r="186" fill="url(#blueTeal)" role="img" aria-label="Embroidery heads and thread cones in blue and teal tones"/>
      <circle class="feature-disc" cx="512" cy="739" r="171" fill="url(#pinkGlow)" role="img" aria-label="Close-up of embroidery machine needles in pink tones"/>

      <rect class="product-photo" x="335" y="96" width="256" height="416" rx="6" fill="url(#machineTone)" role="img" aria-label="Single-head industrial embroidery machine on stand stitching a purple garment"/>
      <rect class="product-photo" x="233" y="664" width="354" height="177" rx="6" fill="url(#machineTone)" role="img" aria-label="Six-head industrial embroidery machine"/>
    </svg>

    <div class="brand brand-primary"><span class="brand-mark"></span>BRANDELL SOLUTIONS</div>
    <div class="brand brand-partner">VELMORA</div>

    <h1 class="title">
      <span>The</span>
      <span class="accent-pink">True Cost</span>
      <span>Of an</span>
      <span class="accent-teal">Embroidery</span>
      <span class="accent-teal">Machine</span>
    </h1>

    <p class="subtitle">Why the Lowest Upfront Price Can Become the Most Expensive Decision</p>
  </article>
</body>
</html>
```